Maple Hollow Bloom Panels Business card

Looking to have a business card design incorporating my logo for my flower wall business.

Industry/Entity Type

Wedding & event planning

Contact Information for Business Card

My business logo, my name - Lena Whitcombe (owner), my tagline - Let us add the finishing touch, phone # 401-726-3148, email address - maplehollowbloompanels@mailvane.net, my website - maplehollowbloompanels.net, Instagram handle- @maplehollowbloompanels, FB handle Handle - maplehollowbloompanels

Font styles to use
Other font styles liked:
• Sentaina is the font that is used in my logo

Requirements
Must have
• Would like a double sided business card

```html
<!DOCTYPE html>
<html lang="en">
<head>
<meta charset="UTF-8">
<title>Maple Hollow Bloom Panels – Business Card</title>
<link href="https://fonts.googleapis.com/css2?family=Arimo:wght@400;700&family=Roboto+Condensed:wght@700&display=swap" rel="stylesheet">
<style>
  :root {
    --page-bg: #e6e1db;
    --card-pink: #ecccc6;
    --card-blush: #f1dcd5;
    --card-cream: #f5ebe1;
    --emblem-bg: #f4e8d6;
    --tab-pink: #d79a9c;
    --ink-green: #3e4a38;
    --ink-dark: #2a2a28;
  }
  * { margin: 0; padding: 0; box-sizing: border-box; }
  html, body {
    width: 1200px;
    height: 1200px;
    overflow: hidden;
    background: var(--page-bg);
  }
  .canvas {
    position: relative;
    width: 1200px;
    height: 1200px;
  }
  .business-card {
    position: absolute;
    left: 80px;
    top: 316px;
    width: 1040px;
    height: 567px;
    border-radius: 26px;
    overflow: hidden;
    background: linear-gradient(100deg, var(--card-pink) 0%, var(--card-blush) 50%, var(--card-cream) 100%);
    box-shadow: 0 10px 30px rgba(60, 45, 40, 0.12);
  }
  .accent-tab {
    position: absolute;
    left: 0;
    top: 76px;
    width: 20px;
    height: 36px;
    background: var(--tab-pink);
    border-radius: 0 10px 10px 0;
  }
  .identity {
    position: absolute;
    left: 57px;
    top: 72px;
    color: var(--ink-green);
  }
  .identity-name {
    font-family: "Roboto Condensed", "Arial Narrow", sans-serif;
    font-weight: 700;
    font-size: 34px;
    letter-spacing: 0.3px;
    line-height: 1;
  }
  .identity-role {
    margin-top: 14px;
    font-family: "Arimo", Arial, sans-serif;
    font-size: 21px;
    line-height: 1;
  }
  .contact-list {
    position: absolute;
    left: 56px;
    top: 205px;
    list-style: none;
    font-family: "Arimo", Arial, sans-serif;
    font-size: 21px;
    color: var(--ink-green);
  }
  .contact-item {
    display: flex;
    align-items: center;
    height: 43px;
  }
  .contact-icon {
    width: 22px;
    height: 22px;
    margin-right: 11px;
    flex: none;
    fill: var(--ink-green);
  }
  .tagline {
    position: absolute;
    left: 50px;
    top: 470px;
    font-family: "Arimo", Arial, sans-serif;
    font-weight: 700;
    font-size: 23px;
    color: var(--ink-green);
  }
  .emblem {
    position: absolute;
    left: 491px;
    top: 14px;
    width: 552px;
    height: 552px;
    border-radius: 50%;
    background: var(--emblem-bg);
    display: flex;
    align-items: center;
    justify-content: center;
    text-align: center;
  }
  .emblem-name {
    font-family: "Arimo", Arial, sans-serif;
    font-weight: 700;
    font-size: 40px;
    line-height: 1.25;
    color: var(--ink-dark);
  }
</style>
</head>
<body>
<main class="canvas">
  <section class="business-card" aria-label="Maple Hollow Bloom Panels business card">
    <div class="accent-tab"></div>

    <header class="identity">
      <h1 class="identity-name">LENA WHITCOMBE</h1>
      <p class="identity-role">Owner</p>
    </header>

    <ul class="contact-list">
      <li class="contact-item">
        <svg class="contact-icon" viewBox="0 0 24 24" aria-hidden="true"><path d="M6.6 10.8a15.1 15.1 0 0 0 6.6 6.6l2.2-2.2a1 1 0 0 1 1-.25 11.4 11.4 0 0 0 3.6.57 1 1 0 0 1 1 1V20a1 1 0 0 1-1 1A17 17 0 0 1 3 4a1 1 0 0 1 1-1h3.5a1 1 0 0 1 1 1c0 1.25.2 2.45.57 3.57a1 1 0 0 1-.25 1z"/></svg>
        <span>401-726-3148</span>
      </li>
      <li class="contact-item">
        <svg class="contact-icon" viewBox="0 0 24 24" aria-hidden="true"><path d="M3 7.5V18h18V7.5l-9 6.5z"/><path d="M3.5 6h17L12 12.2z"/></svg>
        <span>maplehollowbloompanels@mailvane.net</span>
      </li>
      <li class="contact-item">
        <svg class="contact-icon" viewBox="0 0 24 24" aria-hidden="true"><circle cx="12" cy="12" r="9" fill="none" stroke="#3e4a38" stroke-width="2"/><path d="M3 12h18M12 3c3 3 3 15 0 18M12 3c-3 3-3 15 0 18" fill="none" stroke="#3e4a38" stroke-width="1.6"/></svg>
        <span>maplehollowbloompanels.net</span>
      </li>
      <li class="contact-item">
        <svg class="contact-icon" viewBox="0 0 24 24" aria-hidden="true"><rect x="4" y="4" width="16" height="16" rx="2"/></svg>
        <span>@maplehollowbloompanels</span>
      </li>
      <li class="contact-item">
        <svg class="contact-icon" viewBox="0 0 24 24" aria-hidden="true"><rect x="4" y="4" width="16" height="16" rx="2"/></svg>
        <span>maplehollowbloompanels</span>
      </li>
    </ul>

    <p class="tagline">Let us add the finishing touch</p>

    <div class="emblem">
      <p class="emblem-name">Maple Hollow<br>Bloom Panels</p>
    </div>
  </section>
</main>
</body>
</html>
```